Etiketten für Herstellung von Tahini und Helva
Zielgruppe
Verarbeitung Sesam
Herstellung Helva
Beispiel habe ich beigefügt
ANBEI FINDEN SIE NEUES BILD ' IN DIESER RICHTUNG '
Aufgabenstellung
Label Durchmesser ca 12 cm ( Verpackung ist PP Schale durchsichtig) Verpackung bild finden Sie anbei
oben kommt Marke + Bild
unten die Inhaltstoffe usw.
Made in Germany ,
100% Natur
Helva mit Vanillegeschmack, with vanilla aroma, vanilya Aromali
Süße Sesampaste
Traditional türkische Spezialität
Bitte nur Helva als Produktname eintragen

```html
<!DOCTYPE html>
<html lang="de">
<head>
<meta charset="utf-8">
<title>Helva Etiketten</title>
<link href="https://fonts.googleapis.com/css2?family=Marcellus&family=Jost:wght@500&family=Pathway+Gothic+One&display=swap" rel="stylesheet">
<style>
  :root {
    --bg: #ffffff;
    --label-black: #1e1e1c;
    --gold: #dcb466;
    --band: #dfb566;
    --brand-green: #3f8f3c;
    --ring-pistachio: #a9cc12;
    --ring-honey: #f8c900;
    --ring-vanilla: #7b4a2c;
    --badge-ring: #2a241c;
    --badge-fill: #e8cf98;
  }
  * { margin: 0; padding: 0; box-sizing: border-box; }
  html, body { width: 1200px; height: 479px; overflow: hidden; background: var(--bg); }
  .sheet { position: relative; width: 1200px; height: 479px; }

  .label {
    position: absolute;
    width: 368px; height: 368px;
    border-radius: 50%;
    overflow: hidden;
    background: var(--label-black);
    border: 6px solid var(--ring);
  }
  .label--pistachio { left: 30px; top: 31px; --ring: var(--ring-pistachio); }
  .label--honey { left: 420px; top: 29px; --ring: var(--ring-honey); }
  .label--vanilla { left: 804px; top: 31px; --ring: var(--ring-vanilla); }

  .label__inner { position: absolute; left: -6px; top: -6px; width: 368px; height: 368px; }

  .label__band {
    position: absolute; left: 0; right: 0; top: 250px; bottom: 0;
    background: var(--band);
  }

  .brand__mark {
    position: absolute; left: 158px; top: 18px;
    width: 50px; height: 50px; border-radius: 50%;
    background: var(--brand-green);
  }
  .brand__name {
    position: absolute; left: 133px; width: 100px; top: 72px;
    text-align: center;
    font-family: "Marcellus", serif;
    font-size: 15px; letter-spacing: 0.5px;
    color: var(--brand-green);
    white-space: nowrap;
  }

  .product-photo {
    position: absolute; left: 136px; top: 142px;
    width: 212px; height: 160px;
    clip-path: polygon(86px 0, 212px 0, 212px 160px, 0 160px, 0 98px, 86px 98px);
  }
  .product-photo--pistachio { background: radial-gradient(circle at 78% 78%, #8fbf3e 0 22%, transparent 42%), linear-gradient(160deg, #dfc6a8, #c9a886); }
  .product-photo--honey { background: radial-gradient(circle at 70% 75%, #f2a531 0 24%, transparent 44%), linear-gradient(160deg, #dfc6a8, #c9a886); }
  .product-photo--vanilla { background: radial-gradient(circle at 74% 62%, #f6ee76 0 18%, transparent 38%), linear-gradient(160deg, #dfc6a8, #c9a886); }

  .product-name {
    position: absolute; left: 60px; top: 96px;
    font-family: "Jost", sans-serif;
    font-weight: 500;
    font-size: 80px; line-height: 62px; letter-spacing: 0;
    color: var(--gold);
    white-space: nowrap;
  }

  .subtitle {
    position: absolute; left: 115px; width: 100px; top: 160px;
    text-align: center;
    font-family: "Pathway Gothic One", sans-serif;
    font-size: 15px; line-height: 18px; color: var(--gold);
    white-space: nowrap;
  }
  .description {
    position: absolute; left: 20px; width: 222px; top: 183px;
    text-align: center;
    font-family: "Pathway Gothic One", sans-serif;
    font-size: 15px; line-height: 15.5px; color: var(--gold);
    white-space: nowrap;
  }
  .description__line { display: block; }
  .description--staggered { text-align: left; left: 49px; }
  .description__line--i1 { padding-left: 5px; }
  .description__line--i2 { padding-left: 51px; }
  .description__line--i3 { padding-left: 17px; }

  .badges { position: absolute; left: 100px; top: 290px; display: flex; gap: 11px; }
  .badge {
    width: 48px; height: 48px; border-radius: 50%;
    background: var(--badge-fill);
    border: 3px solid var(--badge-ring);
  }
  .badge--dark { background: var(--badge-ring); border-color: var(--badge-fill); box-shadow: 0 0 0 2px var(--badge-ring); }
</style>
</head>
<body>
<main class="sheet">

  <section class="label label--pistachio">
    <div class="label__inner">
      <div class="label__band"></div>
      <div class="brand__mark"></div>
      <div class="brand__name">MONDKORN</div>
      <div class="product-photo product-photo--pistachio" role="img" aria-label="Helva-Block mit Pistazien"></div>
      <div class="product-name">HELVA</div>
      <div class="subtitle">Süße Sesampaste</div>
      <div class="description">
        <span class="description__line">Traditionelle türkische Spezialität</span>
        <span class="description__line">mit Pistazien - with pistacio</span>
        <span class="description__line">Antep fıstık</span>
      </div>
      <div class="badges">
        <div class="badge"></div><div class="badge"></div><div class="badge badge--dark"></div>
      </div>
    </div>
  </section>

  <section class="label label--honey">
    <div class="label__inner">
      <div class="label__band"></div>
      <div class="brand__mark"></div>
      <div class="brand__name">MONDKORN</div>
      <div class="product-photo product-photo--honey" role="img" aria-label="Helva-Block mit Honigwabe und Honiglöffel"></div>
      <div class="product-name">HELVA</div>
      <div class="subtitle">Süße Sesampaste</div>
      <div class="description">
        <span class="description__line">Traditionelle türkische Spezialität</span>
        <span class="description__line">mit Honig&nbsp; - with honey</span>
        <span class="description__line">bal ile</span>
      </div>
      <div class="badges">
        <div class="badge"></div><div class="badge"></div><div class="badge badge--dark"></div>
      </div>
    </div>
  </section>

  <section class="label label--vanilla">
    <div class="label__inner">
      <div class="label__band"></div>
      <div class="brand__mark"></div>
      <div class="brand__name">MONDKORN</div>
      <div class="product-photo product-photo--vanilla" role="img" aria-label="Helva-Block mit Vanilleblüte und Vanilleschoten"></div>
      <div class="product-name">HELVA</div>
      <div class="subtitle">Süße Sesampaste</div>
      <div class="description description--staggered">
        <span class="description__line description__line--i1">Traditionelle türkische Spezialität</span>
        <span class="description__line description__line--i2">mit Vanillegeschmack</span>
        <span class="description__line description__line--i3">with vanilla aroma</span>
        <span class="description__line">Vanilya Aromali</span>
      </div>
      <div class="badges">
        <div class="badge"></div><div class="badge"></div><div class="badge badge--dark"></div>
      </div>
    </div>
  </section>

</main>
</body>
</html>
```